Fast Business Card Project

I need a business card with the name RENATO DUARTE stylized on one side and my email on the other (renatocosta4711@mailnova.com)

Industry/Entity Type

Business

Contact Information for Business Card

www.trilhamar.com.br

```html
<!DOCTYPE html>
<html lang="pt-BR">
<head>
<meta charset="UTF-8">
<title>Cartão de visita — Renato Duarte (verso)</title>
<link href="https://fonts.googleapis.com/css2?family=Archivo:wght@700;800&display=swap" rel="stylesheet">
<style>
  :root {
    --card-bg: #ffffff;
    --ink: #000000;
    --web-grey: #8c8c8c;
  }
  html, body {
    margin: 0;
    padding: 0;
    width: 1200px;
    height: 702px;
    overflow: hidden;
    background: var(--card-bg);
  }
  .card-back {
    position: relative;
    width: 1200px;
    height: 702px;
    background: var(--card-bg);
    overflow: hidden;
  }
  .edge-arc {
    position: absolute;
    inset: 0;
    width: 1200px;
    height: 702px;
  }
  .edge-arc path { fill: var(--ink); }
  .contact {
    position: absolute;
    left: 204px;
    top: 292px;
    font-family: "Archivo", Arial, sans-serif;
  }
  .contact-email {
    margin: 0;
    font-size: 44px;
    font-weight: 700;
    color: var(--ink);
    line-height: 1;
    letter-spacing: 0.2px;
  }
  .contact-web {
    margin: 26px 0 0 2px;
    font-size: 38px;
    font-weight: 800;
    color: var(--web-grey);
    line-height: 1;
    letter-spacing: 2.4px;
  }
</style>
</head>
<body>
  <main class="card-back">
    <svg class="edge-arc" viewBox="0 0 1200 702" aria-hidden="true">
      <path d="M912 0 C1035 150 1120 360 1134 560 L1134 702 L1200 702 L1200 0 Z"/>
    </svg>
    <section class="contact">
      <p class="contact-email">renatocosta4711@mailnova.com</p>
      <p class="contact-web">www.trilhamar.com.br</p>
    </section>
  </main>
</body>
</html>
```